Healthcare Consulting company business card

We are looking for a business card design for a new healthcare consulting company. The company is looking to provide assistance to large healthcare organisations in the following categories:
Acute care and critical care
Tender documents and applications
CV, job applications and interview skills
scientific lecture presentation preparations and skills
research and quality activities
medical equipment and device consulting
hemofiltration liaising.
Please see the attached file below for the design brief.
Alternative designs are welcomed.
Industry/Entity Type
Business
Contact Information for Business Card
Name: Rob Kettering
Mobile: 0427 861 093
Email: robketteringconsulting@mailvale.com
Website: www.robketteringconsulting.com.au

```html
<!DOCTYPE html>
<html lang="en">
<head>
<meta charset="utf-8">
<title>Rob Kettering Consulting – Business Card</title>
<link rel="stylesheet" href="https://fonts.googleapis.com/css2?family=Arimo:wght@400;700&display=swap">
<style>
  :root {
    --brand-blue: #0d55a3;
    --card-white: #ffffff;
    --page-bg: #eef0f3;
    --card-shadow: rgba(20, 30, 50, 0.18);
  }
  * { box-sizing: border-box; margin: 0; padding: 0; }
  html, body {
    width: 1200px;
    height: 800px;
    overflow: hidden;
    background: var(--page-bg);
    font-family: "Arimo", Arial, sans-serif;
  }
  .canvas {
    position: relative;
    width: 1200px;
    height: 800px;
  }
  .card {
    position: absolute;
    left: 330px;
    width: 530px;
    height: 300px;
    border-radius: 10px;
    box-shadow: 0 4px 14px var(--card-shadow);
    overflow: hidden;
  }
  .card--front {
    top: 60px;
    background: var(--brand-blue);
    color: var(--card-white);
  }
  .card--back {
    top: 430px;
    background: var(--card-white);
    color: var(--brand-blue);
  }

  /* Company name set as plain wordmark text */
  .wordmark {
    position: absolute;
    text-align: center;
    font-weight: 700;
    line-height: 1;
  }
  .wordmark__name {
    display: block;
    text-transform: uppercase;
    letter-spacing: 0.02em;
  }
  .wordmark__tagline {
    display: block;
    text-transform: uppercase;
    letter-spacing: 0.3em;
  }
  .card--front .wordmark {
    left: 0;
    right: 0;
    top: 88px;
  }
  .card--front .wordmark__name { font-size: 34px; }
  .card--front .wordmark__tagline { font-size: 17px; margin-top: 8px; padding-left: 0.3em; }

  .card--back .wordmark {
    right: 28px;
    top: 62px;
    width: 170px;
  }
  .card--back .wordmark__name { font-size: 19px; }
  .card--back .wordmark__tagline { font-size: 10px; margin-top: 5px; padding-left: 0.3em; }

  /* Contact block */
  .contact {
    position: absolute;
    left: 34px;
    top: 20px;
    line-height: 1.05;
  }
  .contact__name {
    font-size: 23px;
    font-weight: 400;
    text-transform: uppercase;
    letter-spacing: 0.02em;
    margin-bottom: 3px;
  }
  .contact__line {
    font-size: 17px;
    font-weight: 400;
  }

  /* Service tiles row */
  .services {
    position: absolute;
    left: 58px;
    right: 58px;
    bottom: 40px;
    display: flex;
    justify-content: space-between;
    list-style: none;
  }
  .services__tile {
    width: 50px;
    height: 46px;
  }
  .card--front .services__tile { background: var(--card-white); }
  .card--back .services__tile { background: var(--brand-blue); }
</style>
</head>
<body>
<main class="canvas">

  <section class="card card--front" aria-label="Business card front">
    <div class="wordmark">
      <span class="wordmark__name">Rob Kettering</span>
      <span class="wordmark__tagline">Consulting</span>
    </div>
    <ul class="services">
      <li class="services__tile" role="img" aria-label="Icon: consultant advising a client on tenders"></li>
      <li class="services__tile" role="img" aria-label="Icon: heart with heartbeat line for acute care"></li>
      <li class="services__tile" role="img" aria-label="Icon: patient in hospital bed with monitor"></li>
      <li class="services__tile" role="img" aria-label="Icon: professional with job application documents"></li>
      <li class="services__tile" role="img" aria-label="Icon: microscope and test tubes for research"></li>
    </ul>
  </section>

  <section class="card card--back" aria-label="Business card back">
    <address class="contact" style="font-style: normal;">
      <p class="contact__name">Rob Kettering</p>
      <p class="contact__line">0427 861 093</p>
      <p class="contact__line">robketteringconsulting@mailvale.com</p>
      <p class="contact__line">www.robketteringconsulting.com.au</p>
    </address>
    <div class="wordmark">
      <span class="wordmark__name">Rob Kettering</span>
      <span class="wordmark__tagline">Consulting</span>
    </div>
    <ul class="services">
      <li class="services__tile" role="img" aria-label="Icon: consultant advising a client on tenders"></li>
      <li class="services__tile" role="img" aria-label="Icon: heart with heartbeat line for acute care"></li>
      <li class="services__tile" role="img" aria-label="Icon: patient in hospital bed with monitor"></li>
      <li class="services__tile" role="img" aria-label="Icon: professional with job application documents"></li>
      <li class="services__tile" role="img" aria-label="Icon: microscope and test tubes for research"></li>
    </ul>
  </section>

</main>
</body>
</html>
```